Brightwave Reach - Business Card

We need a business card for a Social Media Marketing company that specializes in online marketing for small businesses in Canada using common Social Media platforms such as Pictora, Kinloop, Blinkit & Chirpo.

I have uploaded a copy of our logo which I would like utilized in the business card. We would like the business card to be modern yet classy design.

Our website is www.brightwavereach.ca

Industry/Entity Type

Marketing

Contact Information for Business Card

Email: info@brightwavereach.ca
Website: www.brightwavereach.ca
Telephone: 604-392-5108

Colors

Designer to choose colors to be used in the design.

Requirements
Must have
• Social Media icons on reverse
• Please add some designs with color.

```html
<!DOCTYPE html>
<html lang="en">
<head>
<meta charset="utf-8">
<title>Brightwave Reach – Business Card</title>
<link href="https://fonts.googleapis.com/css2?family=Open+Sans:wght@400;600;800&display=swap" rel="stylesheet">
<style>
  :root {
    --stage: #2a2a2b;
    --card: #f4f4f2;
    --ink: #3a3a3a;
    --ink-soft: #8f8f8f;
    --leaf: #4a4a4a;
  }
  * { margin: 0; padding: 0; box-sizing: border-box; }
  html, body {
    width: 1200px; height: 840px; overflow: hidden;
    background: var(--stage);
    font-family: "Open Sans", Arial, sans-serif;
    color: var(--ink);
  }
  .stage {
    position: relative; width: 1200px; height: 840px;
    display: flex; align-items: center; justify-content: center; gap: 40px;
  }
  .card {
    position: relative; width: 540px; height: 309px;
    background: var(--card);
    box-shadow: 0 10px 30px rgba(0,0,0,.45);
  }

  /* Logo side */
  .card--logo { display: flex; align-items: center; justify-content: center; }
  .logo-lockup { display: flex; align-items: center; gap: 14px; }
  .logo-square { width: 22px; height: 22px; border: 3px solid var(--ink); }
  .logo-name {
    font-weight: 800; font-size: 30px; letter-spacing: .5px;
    text-transform: uppercase; color: var(--ink);
  }

  /* Contact side */
  .frame { position: absolute; inset: 0; width: 100%; height: 100%; }
  .contact-block { position: absolute; left: 56px; top: 52px; }
  .brand-title {
    font-weight: 800; font-size: 38px; line-height: 36px;
    text-transform: uppercase; color: var(--ink); letter-spacing: .3px;
  }
  .person-name {
    margin-top: 22px; font-weight: 600; font-size: 14px;
    text-transform: uppercase; letter-spacing: .4px;
  }
  .person-role {
    font-size: 13px; color: var(--ink-soft); text-transform: uppercase;
    letter-spacing: .4px;
  }
  .contact-lines { margin-top: 10px; font-size: 13px; line-height: 19px; }
  .social-row { display: flex; gap: 12px; margin-top: 10px; }
  .social-item { display: flex; align-items: center; gap: 4px; font-size: 10px; }
  .social-dot {
    width: 10px; height: 10px; border-radius: 50%;
    border: 1.5px solid var(--ink);
  }
  .leaf-art {
    position: absolute; right: 60px; bottom: 48px;
    width: 140px; height: 140px;
    background: radial-gradient(circle at 50% 45%, var(--leaf) 0%, #5e5e5e 60%, transparent 71%);
  }
</style>
</head>
<body>
<main class="stage">
  <section class="card card--logo" aria-label="Business card back">
    <div class="logo-lockup">
      <span class="logo-square"></span>
      <span class="logo-name">Brightwave Reach</span>
    </div>
  </section>

  <section class="card card--contact" aria-label="Business card front">
    <svg class="frame" viewBox="0 0 540 309" aria-hidden="true">
      <rect x="22" y="20" width="496" height="269" fill="none" stroke="#3a3a3a" stroke-width="4"/>
      <rect x="32" y="30" width="476" height="249" fill="none" stroke="#3a3a3a" stroke-width="1.5"/>
    </svg>
    <div class="contact-block">
      <h1 class="brand-title">Brightwave<br>Reach</h1>
      <p class="person-name">Daniel Reyes</p>
      <p class="person-role">CEO/Founder</p>
      <p class="contact-lines">
        604-392-5108<br>
        info@brightwavereach.ca<br>
        www.brightwavereach.ca
      </p>
      <div class="social-row">
        <span class="social-item"><span class="social-dot"></span>Kinloop</span>
        <span class="social-item"><span class="social-dot"></span>Pictora</span>
        <span class="social-item"><span class="social-dot"></span>Chirpo</span>
      </div>
    </div>
    <div class="leaf-art" role="img" aria-label="Distressed dark grey maple leaf illustration"></div>
  </section>
</main>
</body>
</html>
```